Comprehensive Brand Identity System for Nalvi Scrubs

Nalvi Scrubs is a fast-growing Mexican brand specializing in medical uniforms. With 4 years in the market and a strong position in the eCommerce space, we've built a solid customer base and brand presence. However, our rapid growth has led to a visual identity developed more by reaction than by design.

We are now looking to take a strategic step forward by launching a comprehensive branding project aimed at unifying all visual assets under one cohesive concept that reflects our brand’s essence: professional, clear, and fun.

Project Scope:

We are seeking a visual identity system that includes the redesign and alignment of the following brand assets:

Product labels

Delivery packaging and bags

Mailers

Thank-you cards

Promotional stickers

Icon set for web and social media

A complete Brand Guidelines Manual (brand book), outlining the visual system: color palette, typography, photography style, graphic rules, and usage guidelines.

Goal:

Create a cohesive and lasting visual identity that strengthens our brand presence and delivers a consistent experience across all touchpoints. The design should strike a balance between clean professionalism and approachable, playful energy that resonates with our core audience — healthcare professionals who value both function and style.

Design Direction:

We want the brand to feel vibrant, modern, and human — while still reflecting the trust and quality expected in the medical field.
Updates

Low design quality

Target Market(s)

Our target market consists of healthcare professionals — including doctors, nurses, medical assistants, dentists, and veterinarians.

Industry/Entity Type

medical apparel

Font styles to use
Sans Serif

Colors
0094D4
00A9DD
6FCCEA
C7EBF8
E9F6FB
EE7325
F08F49
F5BC92
FAE3D3
FDF4ED
E54698
E96AAD
F1A4CE
F9D9EA
FCEFF6
A7469A
B969AE
D3A5CF
EDDBEB
F8F0F9
6B429C
8869AF
B7A5CE
E3DAEB
F3F0F8

Requirements
Must have
• We want the brand to feel vibrant, modern, and human — while still reflecting the trust and quality expected in the medical field.

```html
<!DOCTYPE html>
<html lang="es">
<head>
<meta charset="utf-8">
<title>Nalvi Scrubs — Brand Proposal Guidelines</title>
<link rel="stylesheet" href="https://fonts.googleapis.com/css2?family=Poppins:wght@400;500;600&family=Playfair+Display:ital,wght@0,400;1,400&family=Courier+Prime&family=Shrikhand&family=Bagel+Fat+One&family=Tinos&display=swap">
<style>
  :root{
    --sand:#e6dccb;
    --khaki:#bea886;
    --ink:#231a13;
    --logo:#3a3a3a;
    --rule:#9a948c;
    --white:#ffffff;
    --violet:#9189c2;
    --pink:#ec6aa2;
    --blue:#5a84c6;
    --peach:#f4aa82;
    --cloud:#f2f2f4;
    --graphite:#4b4a4b;
  }
  *{box-sizing:border-box;margin:0;padding:0}
  html,body{width:1055px;height:1200px;overflow:hidden;background:var(--white)}
  body{position:relative;font-family:"Poppins",sans-serif;color:var(--ink)}
  .slide{position:absolute;width:505px;height:284px;overflow:hidden}
  .col-l{left:13px}.col-r{left:528px}
  .row-1{top:9px}.row-2{top:304px}.row-3{top:598px}.row-4{top:892px}
  .sand{background:var(--sand)}
  .khaki{background:var(--khaki)}
  .plain{background:var(--white)}
  .brand-name{position:absolute;left:12px;top:9px;font:600 16px/1 "Poppins",sans-serif;color:var(--logo);letter-spacing:-.3px}
  .abs{position:absolute}
  .title-sans{font:400 44px/1 "Poppins",sans-serif;letter-spacing:-.5px}
  .title-serif{font:italic 400 50px/1 "Playfair Display",serif;letter-spacing:-1px}
  .head-sans{font:400 34px/1 "Poppins",sans-serif}
  .head-serif{font:italic 400 36px/1 "Playfair Display",serif}
  .bullets{list-style:none;font:400 8.4px/13.7px "Poppins",sans-serif}
  .bullets li::before{content:"•";display:inline-block;width:12px}
  .photo{position:absolute}
  .dark-block{position:absolute;background:var(--ink)}
  .vertical{position:absolute;left:18px;top:52px;transform-origin:left top;transform:rotate(90deg) translateY(-50px);white-space:nowrap}
  .vertical .v1{font:400 22px/1 "Poppins",sans-serif;display:block}
  .vertical .v2{font:italic 400 24px/1 "Playfair Display",serif;display:block;margin-top:2px}
  .rule{position:absolute;height:0;border-top:.6px solid var(--rule)}
  .intro{font:400 8.6px/13.6px "Poppins",sans-serif}
  .ref{position:absolute;display:flex;align-items:center;gap:9px;font:400 9px/1 "Poppins",sans-serif}
  .ref::before{content:"";width:20px;height:20px;border:.8px solid var(--ink);border-radius:50%}
  .propuesta{position:absolute;left:15px;top:158px;font:400 52px/1 "Playfair Display",serif;color:#fbf6ee;letter-spacing:1px}
  .section-tag{position:absolute;left:136px;top:17px;font:500 4.6px/1 "Poppins",sans-serif;letter-spacing:.2px}
  .lead{position:absolute;left:15px;top:63px;font:italic 400 9.5px/11.5px "Poppins",sans-serif}
  .lead b{font:400 9.5px/11.5px "Tinos",serif}
  .mono{position:absolute;left:15px;font:400 4.7px/6.8px "Courier Prime",monospace;width:86px}
  .swatch{position:absolute;width:115px;height:82px}
  .swatch span{position:absolute;left:7px;bottom:15px;font:400 5.2px/1 "Tinos",serif;color:rgba(255,255,255,.9)}
  .swatch.light span{color:#9a9aa0}
  .grad{position:absolute;top:237px;width:171px;height:16px}
  .font-label{position:absolute;left:136px;font:400 4.4px/1 "Tinos",serif}
  .font-sample{position:absolute;left:136px}
  .s-poppins{font:400 34px/1 "Poppins",sans-serif}
  .s-shrik{font:400 26px/1 "Shrikhand",cursive;color:#1f1a17}
  .s-bagel{font:400 30px/1 "Bagel Fat One",cursive;color:#1f1a17}
  .tile{position:absolute}
</style>
</head>
<body>

<section class="slide sand col-l row-1">
  <div class="brand-name">Nalvi.</div>
  <div class="abs title-sans" style="left:14px;top:98px">BRAND PROPOSAL</div>
  <div class="abs title-serif" style="left:14px;top:138px">GUIDELINES</div>
</section>

<section class="slide sand col-r row-1">
  <div class="brand-name">Nalvi.</div>
  <ul class="abs bullets" style="left:20px;top:91px">
    <li>Base divertida y cercana</li>
    <li>Energía joven y disruptiva</li>
    <li>Elementos reconocibles (Logo &amp; Degradados)</li>
    <li>lenguaje gráfico propio &gt; retro optimism</li>
    <li>Transmita confianza, calidad y profesionalismo</li>
    <li>Diferenciación clara en el mercado</li>
  </ul>
  <div class="abs head-sans" style="left:16px;top:201px">WHAT IS</div>
  <div class="abs head-serif" style="left:16px;top:235px">WORKING</div>
  <div class="photo" role="img" aria-label="Fotografía: profesional atando un gorro quirúrgico negro con estampado rosa" style="left:310px;top:0;width:195px;height:195px;background:linear-gradient(160deg,#e9e9ea 0%,#2a2328 45%,#c97fb6 70%,#1d181b 100%)"></div>
  <div class="dark-block" style="left:310px;top:195px;width:195px;height:89px"></div>
</section>

<section class="slide sand col-l row-2">
  <div class="brand-name">Nalvi.</div>
  <ul class="abs bullets" style="left:20px;top:91px">
    <li>Inconsistencia Visual General</li>
    <li>Hilo Conductor Visual</li>
    <li>Paleta de Color sin Sistema Definido</li>
    <li>Desbalance Diversión y Profesionalismo</li>
    <li>Fotografía y Estilo Visual No Definidos</li>
    <li>Iconografía Dispersa</li>
  </ul>
  <div class="abs head-sans" style="left:16px;top:201px">WHAT CAN</div>
  <div class="abs head-serif" style="left:16px;top:235px">BE BETTER</div>
  <div class="photo" role="img" aria-label="Fotografía: dos profesionales sentados con uniformes naranja y verde azulado" style="left:310px;top:0;width:195px;height:284px;background:linear-gradient(180deg,#d9d9de 0%,#c9c6c8 35%,#d77a4e 60%,#2c7f8a 80%,#e4e4e6 100%)"></div>
</section>

<section class="slide sand col-r row-2">
  <div class="brand-name">Nalvi.</div>
  <div class="vertical"><span class="v1">MARCAS DE</span><span class="v2">REFERENCIA</span></div>
  <div class="rule" style="left:135px;top:32px;width:354px"></div>
  <p class="abs intro" style="left:135px;top:60px">Algunas marcas que nos pueden servir como<br>referencias a la hora de pensar en la marca.</p>
  <div class="ref" style="left:135px;top:107px">LUMEN</div>
  <div class="ref" style="left:280px;top:107px">PETALWISE</div>
  <div class="ref" style="left:135px;top:136px">CONTRARA</div>
  <div class="ref" style="left:280px;top:136px">HOLA MARLO</div>
  <div class="ref" style="left:135px;top:171px">CORTEJO</div>
  <div class="ref" style="left:280px;top:171px">ANISA</div>
  <div class="photo" role="img" aria-label="Fotografía: grupo de cuatro profesionales con chaquetas negras" style="left:135px;top:211px;width:370px;height:73px;background:linear-gradient(90deg,#c4d0dc 0%,#b8c5d2 25%,#1e1e22 45%,#2a2a2e 70%,#c2ccd6 100%)"></div>
</section>

<section class="slide khaki col-l row-3">
  <div class="photo" role="img" aria-label="Fotografía: grupo sonriente de profesionales con uniformes de colores" style="left:0;top:0;width:505px;height:85px;background:linear-gradient(90deg,#e6e6e6 0%,#3b6bb0 25%,#3e6a4a 38%,#c0264a 52%,#e04a78 65%,#d8cdbf 80%,#e8e8e8 100%)"></div>
  <div class="propuesta">PROPUESTA</div>
</section>

<section class="slide plain col-r row-3">
  <div class="brand-name">Nalvi.</div>
  <div class="section-tag">COLOR GUIDELINES</div>
  <div class="rule" style="left:136px;top:32px;width:353px"></div>
  <p class="lead">THE &nbsp;NEW COLOR<br>OF <b>NALVI.</b></p>
  <p class="mono" style="top:110px">La paleta de Nalvi Scrubs equilibra profesionalismo y frescura. Los tonos lilas, rosas y melocotón aportan energía y cercanía, mientras que el azul, el blanco suave y el gris grafito refuerzan la confianza y la claridad visual. El resultado: una marca vibrante, moderna y coherente.</p>
  <div class="swatch" style="left:136px;top:60px;background:var(--violet)"><span>NALVI VIOLET</span></div>
  <div class="swatch" style="left:255px;top:60px;background:var(--pink)"><span>PULSE PINK</span></div>
  <div class="swatch" style="left:374px;top:60px;background:var(--blue)"><span>VITAL BLUE</span></div>
  <div class="swatch" style="left:136px;top:146px;background:var(--peach)"><span>ENERGY PEACH</span></div>
  <div class="swatch light" style="left:255px;top:146px;background:var(--cloud)"><span>NEUTRAL CLOUD</span></div>
  <div class="swatch" style="left:374px;top:146px;background:var(--graphite)"><span>GRAPHITE BLACK</span></div>
  <div class="grad" style="left:136px;background:linear-gradient(90deg,var(--pink),var(--violet) 50%,var(--blue))"></div>
  <div class="grad" style="left:318px;background:linear-gradient(90deg,var(--peach),var(--cloud) 50%,var(--blue))"></div>
</section>

<section class="slide plain col-l row-4">
  <div class="brand-name">Nalvi.</div>
  <div class="section-tag">TYPOGRAPHY</div>
  <div class="rule" style="left:136px;top:32px;width:353px"></div>
  <p class="lead">THE NEW TYPE<br>OF <b>NALVI</b></p>
  <p class="mono" style="top:146px">La tipografía de Nalvi Scrubs equilibra profesionalismo y personalidad. Poppins aporta claridad y estructura, Shrikhand introduce cercanía y calidez, y Bagel Fat One añade un toque distintivo y enérgico para mensajes clave.</p>
  <div class="font-label" style="top:55px">PRIMARY FONT</div>
  <div class="font-sample s-poppins" style="top:66px">POPPINS</div>
  <div class="font-label" style="top:130px">SECONDARY FONT</div>
  <div class="font-sample s-shrik" style="top:140px">Shrikhand</div>
  <div class="font-label" style="top:205px">SPECIAL FONT</div>
  <div class="font-sample s-bagel" style="top:214px">Bagel Fat One</div>
</section>

<section class="slide plain col-r row-4">
  <div class="brand-name">Nalvi.</div>
  <div class="section-tag">IMAGERY</div>
  <div class="rule" style="left:136px;top:32px;width:353px"></div>
  <p class="lead">THE NEW IMAGE<br>OF <b>NALVI</b></p>
  <div class="tile" role="img" aria-label="Etiqueta de producto talla XL en tonos crema y rosa" style="left:136px;top:46px;width:90px;height:114px;background:linear-gradient(160deg,#f4efe6,#ece3d6 60%,#e9a0b9)"></div>
  <div class="tile" role="img" aria-label="Plancha de stickers promocionales retro en rosa, lila y naranja" style="left:231px;top:46px;width:174px;height:114px;background:linear-gradient(135deg,#3a3466,#6b4f9a 40%,#e86aa5 70%,#f4a270)"></div>
  <div class="tile" role="img" aria-label="Set de iconos de tejido en degradado rosa y azul" style="left:411px;top:46px;width:94px;height:114px;background:linear-gradient(160deg,#f7f5f8,#ece7f3)"></div>
  <div class="tile" role="img" aria-label="Caja de envío con degradado rosa a azul y stickers" style="left:136px;top:166px;width:175px;height:114px;background:linear-gradient(135deg,#e3e4e8 0%,#d98fc9 35%,#7f9be0 70%,#e4e5ea 100%)"></div>
  <div class="tile" role="img" aria-label="Tarjeta de agradecimiento con letras retro melocotón sobre degradado lila y rosa" style="left:316px;top:166px;width:115px;height:103px;background:linear-gradient(160deg,#9a86cf,#e785b6)"></div>
</section>

</body>
</html>
```